First Birthday Party Invitation

We need a flyer/invitation design for our baby girl Marisol's first birthday party. We want the design to look like a club event flyer. The party will have a sailing/nautical theme and will be at a marina but in Miami so the invite must have a cool, non-baby, non-kitchy vibe.

Here's the text...feel free to play around with it!

Welcome Aboard! 

We'll have lots of fun

Our little Marisol is turning one!

You're invited to a party

on Saturday, August 7th from 5 - 7 p.m.

Tide-And-Sail Miami

Third Floor
4815 North Coralwood Lane
Miami, FL 33187-2091
Parking tickets will be validated 

Please RSVP by July 31st to MarisolParty@examplemail.test or 305.555.0172

Arrive early at 4 p.m. to join us on a short pre-party boat tour of the Miami skyline

Flyer should be one-sided only.  It will be printed in color and also emailed. 

Important update - please add small text that says "No gifts please.  A contribution to Tide And Sail's programs would be greatly appreciated."

```html
<!DOCTYPE html>
<html lang="en">
<head>
<meta charset="utf-8">
<title>Marisol's First Birthday – Welcome Aboard</title>
<link rel="stylesheet" href="https://fonts.googleapis.com/css2?family=Anton&family=Fredoka:wght@600&family=Kaushan+Script&family=Ubuntu:wght@400;500;700&display=swap">
<style>
  :root {
    --night-deep: #0a1a5c;
    --night-mid: #1f3fb0;
    --night-glow: #3d5fe0;
    --band: #1a3aa8;
    --ice: #8fe6f5;
    --ice-soft: #b9e6ff;
    --salmon: #f59a86;
    --white: #ffffff;
    --muted: #c5cbe6;
    --outline: #1b3fc4;
  }
  * { margin: 0; padding: 0; box-sizing: border-box; }
  html, body { width: 960px; height: 1200px; overflow: hidden; background: var(--night-deep); }
  .flyer {
    position: relative; width: 960px; height: 1200px; overflow: hidden;
    background: radial-gradient(ellipse 70% 45% at 55% 48%, var(--night-glow) 0%, var(--night-mid) 45%, var(--night-deep) 100%);
    font-family: "Ubuntu", sans-serif;
  }
  .wave-header {
    position: absolute; left: 0; top: 0; width: 960px; height: 140px;
    background: linear-gradient(180deg, #2a4cc0 0%, #3f86d8 40%, #1d3aa6 100%);
  }
  .welcome {
    position: absolute; left: 0; top: 8px; width: 960px; text-align: center;
    font-family: "Fredoka", sans-serif; font-weight: 600; font-style: italic;
    font-size: 76px; color: var(--white);
    -webkit-text-stroke: 4px var(--outline); paint-order: stroke fill;
  }
  .tagline-band {
    position: absolute; left: 0; top: 140px; width: 960px; height: 120px;
    background: linear-gradient(180deg, var(--band) 0%, #2b52d0 50%, var(--band) 100%);
  }
  .tagline {
    position: absolute; color: var(--white); font-weight: 500;
    text-shadow: 2px 2px 3px rgba(0,0,20,.7); white-space: nowrap;
  }
  .tagline.fun { left: 24px; top: 154px; font-size: 40px; }
  .tagline.turning { left: 40px; top: 192px; font-size: 46px; }
  .invited {
    position: absolute; left: 47px; top: 288px;
    font-family: "Anton", sans-serif; font-size: 88px; line-height: 1;
    color: var(--ice); letter-spacing: -1px;
  }
  .to-party {
    position: absolute; left: 193px; top: 362px;
    font-family: "Kaushan Script", cursive; font-size: 58px; color: var(--ice);
  }
  .date-group { position: absolute; left: 20px; top: 445px; width: 620px; height: 110px; }
  .brace { position: absolute; top: -6px; font-size: 110px; line-height: 1; color: #7d8ce0; font-weight: 300; }
  .brace.open { left: 0; }
  .brace.close { left: 585px; }
  .date-line { position: absolute; left: 40px; font-size: 37px; font-weight: 500; color: var(--salmon); white-space: nowrap; }
  .date-line.day { top: 6px; }
  .date-line.time { top: 58px; }
  .venue { position: absolute; left: 60px; top: 574px; color: var(--ice-soft); font-weight: 500; }
  .venue p { font-size: 33px; line-height: 48px; white-space: nowrap; }
  .venue .parking { font-size: 25px; line-height: 36px; color: var(--ice); }
  .harbor-scene {
    position: absolute; left: 0; top: 720px; width: 960px; height: 320px;
    background: linear-gradient(180deg, rgba(40,70,170,0) 0%, #2c4fb8 30%, #5a7fe0 58%, #1c2f8a 70%, #0c1b62 100%);
  }
  .brand {
    position: absolute; left: 660px; top: 560px; width: 260px;
    font-family: "Ubuntu", sans-serif; font-weight: 700; font-size: 40px; line-height: 46px;
    color: var(--ice);
  }
  .rsvp-box {
    position: absolute; left: 24px; top: 787px; width: 556px; height: 170px;
    border-radius: 14px; background: rgba(140,160,230,.32);
    padding: 26px 36px; color: var(--ice-soft); font-size: 27px; line-height: 38px; font-weight: 500;
  }
  .pre-party {
    position: absolute; left: 44px; top: 1038px; color: var(--white);
    font-size: 24px; line-height: 36px; font-weight: 500;
  }
  .note {
    position: absolute; left: 44px; top: 1132px; color: var(--muted); font-size: 17px;
  }
</style>
</head>
<body>
  <main class="flyer">
    <div class="wave-header" role="img" aria-label="Soft blue ocean wave banner"></div>
    <h1 class="welcome">Welcome aboard!</h1>

    <div class="tagline-band"></div>
    <p class="tagline fun">We'll have lots of fun</p>
    <p class="tagline turning">Our little Marisol is turning one!</p>

    <div class="harbor-scene" role="img" aria-label="Night photo of the Miami skyline across the bay with a sailboat on the water"></div>

    <h2 class="invited">YOU'RE INVITED</h2>
    <p class="to-party">to a party</p>

    <div class="date-group">
      <span class="brace open">{</span>
      <p class="date-line day">on Saturday, August 7th</p>
      <p class="date-line time">from 5 - 7 p.m.</p>
      <span class="brace close">}</span>
    </div>

    <address class="venue" style="font-style:normal">
      <p>Third Floor</p>
      <p>4815 North Coralwood Lane</p>
      <p>Miami, FL 33187-2091</p>
      <p class="parking">Parking tickets will be validated</p>
    </address>

    <p class="brand">Tide-And-Sail<br>Miami</p>

    <div class="rsvp-box">
      <p>Please RSVP by July 31st to:</p>
      <p>MarisolParty@examplemail.test</p>
      <p>or 305.555.0172</p>
    </div>

    <p class="pre-party">Arrive early at 4 p.m. to join us<br>on a short pre-party boat tour of the Miami skyline.</p>

    <p class="note">No gifts please.&nbsp; A contribution to Tide And Sail's programs would be greatly appreciated.</p>
  </main>
</body>
</html>
```